Stella Marina packaging design

Hi there,
I'm trying to get an outstanding and unique design for my new product.I'm in baby products business.We are launching an organic,100% burp cloth for our online store. The packaging design is very important to our business.We are looking for something simple and unique.Our brand name is Stella Marina which means Sea Star in Italian. We also have dolphin prints on the burp cloth. Our burp cloth made of organic, hypoallergenic, breathable and ultra soft 100% cotton.Each box has 5 burp cloth. Its made with love and care for delicate and sensitive baby skin.I will attach samples of the burp cloth colors for you to get an idea about the product.

baby product

• Our Logo, ORVA image , and made of organic, hypoallergenic, breathable and ultra soft 100% cotton,has 5 burp cloth. Its made with love and care for delicate and sensitive baby skin.I will attach samples of the burp cloth colors for you to get an idea about the product.
• We are looking for something different and can Standout , please to don't make design that has the exact idea of the template that I provide.

```html
<!DOCTYPE html>
<html lang="en">
<head>
<meta charset="utf-8">
<title>Stella Marina – Baby Burp Cloth Box</title>
<link rel="stylesheet" href="https://fonts.googleapis.com/css2?family=Josefin+Sans:wght@400;600;700&family=Parisienne&display=swap">
<style>
  :root{
    --backdrop:#e7e4df;
    --kraft:#bda684;
    --kraft-dark:#a8916f;
    --teal:#5fae9e;
    --teal-deep:#0f5a63;
    --teal-ink:#116a73;
    --ink:#3a3024;
    --cream:#e9d9b8;
    --cloth:#f4f6f8;
    --cloth-line:#dfe3e8;
    --badge:#2f8a3a;
  }
  html,body{margin:0;padding:0;overflow:hidden;}
  body{width:1200px;height:1200px;background:var(--backdrop);font-family:"Josefin Sans",sans-serif;}
  .box{position:absolute;left:150px;top:70px;width:900px;}
  .lid{position:relative;width:900px;height:800px;background:var(--kraft);overflow:hidden;}
  .certificate-badge{position:absolute;left:40px;top:30px;width:74px;height:74px;border-radius:50%;background:#f3eee3;border:4px solid var(--badge);}
  .title-block{position:absolute;right:40px;top:40px;text-align:right;}
  .title-block h1{margin:0;font-size:50px;font-weight:700;color:var(--teal-ink);letter-spacing:2px;}
  .title-block p{margin:6px 0 0;font-size:18px;font-weight:600;color:var(--ink);letter-spacing:1px;text-transform:uppercase;}
  .window{position:absolute;left:90px;top:140px;width:720px;height:500px;background:var(--cloth);border-radius:6px;box-shadow:inset 0 0 0 2px var(--kraft-dark);}
  .window .fold-v{position:absolute;left:50%;top:0;bottom:0;border-left:2px solid var(--cloth-line);}
  .window .fold-h{position:absolute;top:50%;left:0;right:0;border-top:2px solid var(--cloth-line);}
  .band{position:absolute;left:0;right:0;top:320px;height:170px;background:var(--teal);display:flex;align-items:center;justify-content:space-between;padding:0 70px;box-sizing:border-box;}
  .features{display:flex;gap:28px;}
  .feature{display:flex;flex-direction:column;align-items:center;width:90px;}
  .feature svg{width:56px;height:56px;}
  .feature span{margin-top:6px;font-size:14px;font-weight:600;line-height:1.1;text-align:center;color:var(--ink);text-transform:uppercase;}
  .brand-seal{width:210px;height:210px;border-radius:50%;background:var(--kraft);display:flex;flex-direction:column;align-items:center;justify-content:center;gap:12px;}
  .brand-seal .dot{width:22px;height:22px;border-radius:50%;background:var(--ink);}
  .brand-seal .name{font-size:26px;font-weight:600;color:var(--ink);}
  .pack-count{position:absolute;right:20px;top:520px;width:110px;height:110px;border-radius:50%;background:var(--teal);color:var(--ink);display:flex;flex-direction:column;align-items:center;justify-content:center;text-transform:uppercase;}
  .pack-count strong{font-size:40px;line-height:1;}
  .pack-count span{font-size:12px;font-weight:700;text-align:center;line-height:1.1;}
  .waves{position:absolute;left:0;right:0;bottom:0;height:150px;}
  .tagline{position:absolute;left:70px;bottom:30px;font-family:"Parisienne",cursive;font-size:54px;color:var(--cream);}
  .front{height:230px;background:linear-gradient(90deg,var(--teal-deep),#15707a 70%,var(--teal));padding:40px 70px;box-sizing:border-box;color:var(--cream);}
  .front h2{margin:0;font-size:68px;font-weight:400;letter-spacing:3px;}
  .front p{margin:10px 0 0;font-size:24px;letter-spacing:2px;text-transform:uppercase;}
</style>
</head>
<body>
  <div class="box">
    <section class="lid">
      <div class="certificate-badge" aria-label="ORVA organic certificate badge"></div>
      <div class="title-block">
        <h1>BABY BURP CLOTH</h1>
        <p>Suitable for baby delicate sensitive skin</p>
      </div>
      <div class="window"><div class="fold-v"></div><div class="fold-h"></div></div>
      <div class="band">
        <div class="features">
          <div class="feature">
            <svg viewBox="0 0 56 56"><circle cx="28" cy="28" r="25" fill="none" stroke="#3a3024" stroke-width="2"/><circle cx="28" cy="28" r="8" fill="none" stroke="#3a3024" stroke-width="2"/></svg>
            <span>100%<br>Cotton</span>
          </div>
          <div class="feature">
            <svg viewBox="0 0 56 56"><circle cx="28" cy="28" r="25" fill="none" stroke="#3a3024" stroke-width="2"/><path d="M28 14 C22 24 20 28 20 32 a8 8 0 0 0 16 0 C36 28 34 24 28 14Z" fill="none" stroke="#3a3024" stroke-width="2"/></svg>
            <span>Super<br>Absorbent</span>
          </div>
        </div>
        <div class="brand-seal">
          <div class="dot"></div>
          <div class="name">Stella Marina</div>
        </div>
        <div class="features">
          <div class="feature">
            <svg viewBox="0 0 56 56"><circle cx="28" cy="28" r="25" fill="none" stroke="#3a3024" stroke-width="2"/><path d="M16 40 C20 24 30 16 42 14 C40 28 32 36 16 40Z M16 40 L34 22" fill="none" stroke="#3a3024" stroke-width="2"/></svg>
            <span>Ultra<br>Soft</span>
          </div>
          <div class="feature">
            <svg viewBox="0 0 56 56"><circle cx="28" cy="28" r="25" fill="none" stroke="#3a3024" stroke-width="2"/><path d="M28 42 C16 34 16 22 28 14 C40 22 40 34 28 42Z M28 18 V42" fill="none" stroke="#3a3024" stroke-width="2"/></svg>
            <span>Hypo<br>Allergenic</span>
          </div>
        </div>
      </div>
      <div class="pack-count"><strong>5</strong><span>Burp cloth<br>per pack</span></div>
      <svg class="waves" viewBox="0 0 900 150" preserveAspectRatio="none">
        <path d="M0 40 C200 0 380 90 560 60 C700 38 800 80 900 70 V150 H0Z" fill="#2f8c8a" opacity="0.55"/>
        <path d="M0 80 C180 50 360 120 540 95 C700 75 800 110 900 105 V150 H0Z" fill="#0f5a63"/>
      </svg>
      <div class="tagline">Made with love for little ones</div>
    </section>
    <section class="front">
      <h2>BABY BURP CLOTH</h2>
      <p>Suitable for baby delicate sensitive skin</p>
    </section>
  </div>
</body>
</html>
```